Redesign a Shopify Banner for a spiritual streetwear brand

Redesign Shopify banner for a brand called Vorel Studios we are a spiritually inspired streetwear brand that makes lots of designs with spiritual symbols and space aesthetics like stars. I would like the banner redesigned with the star print I included in this file in the background of the banner with our logo and tag line "spiritually inspired streetwear". you can choose a new font for the banner that could be more aesthetically pleasing. you could also included other alchemical and occult or witchy symbols on the banner along with the stars. or just create the banner with the stars I included in this file. Looking forward to see your work! Thank You.
our website right now is vorel-studios.example

```html
<!DOCTYPE html>
<html lang="en">
<head>
<meta charset="utf-8">
<title>Vorel Studios — Spiritually Inspired Streetwear</title>
<link rel="stylesheet" href="https://fonts.googleapis.com/css2?family=Fredoka:wght@600&family=Gochi+Hand&family=Source+Code+Pro:wght@400&display=swap">
<style>
  :root {
    --night: #000000;
    --night-soft: #0b0b0b;
    --ink: #ffffff;
    --ink-soft: #f2f2f2;
    --nav-text: #c9c9c9;
    --symbol-light: #d8d8d8;
    --symbol-mid: #8a8a8a;
    --symbol-dark: #4a4a4a;
  }
  * { margin: 0; padding: 0; box-sizing: border-box; }
  html, body { width: 1200px; height: 860px; overflow: hidden; background: var(--night); }
  .banner { position: relative; width: 1200px; height: 860px; background: var(--night); }

  .star-field {
    position: absolute; left: 0; top: 140px; width: 1200px; height: 720px;
    background: radial-gradient(ellipse at 50% 50%, var(--night-soft) 0%, var(--night) 75%);
  }

  .site-header { position: absolute; left: 0; top: 0; width: 1200px; height: 140px; }
  .brand-name {
    position: absolute; left: 59px; top: 52px;
    font-family: 'Fredoka', sans-serif; font-weight: 600; font-size: 34px;
    color: var(--ink); letter-spacing: 0.5px; white-space: nowrap;
  }
  .main-nav { position: absolute; top: 70px; left: 0; }
  .main-nav a {
    position: absolute; white-space: nowrap;
    font-family: 'Source Code Pro', monospace; font-size: 12.5px;
    color: var(--nav-text); text-decoration: none;
  }
  .main-nav a.is-current { color: var(--ink); text-decoration: underline; text-underline-offset: 4px; }
  .header-icons { position: absolute; top: 66px; left: 955px; }
  .header-icons svg { position: absolute; top: 0; }

  .illustration { position: absolute; border-radius: 50%; }
  .planet { left: 994px; top: 197px; width: 144px; height: 84px;
    background: radial-gradient(ellipse, #1a1a1a 0%, rgba(0,0,0,0) 70%); }
  .constellation { left: 44px; top: 609px; width: 144px; height: 204px; border-radius: 40%;
    background: radial-gradient(ellipse, #161616 0%, rgba(0,0,0,0) 70%); }

  .symbols { position: absolute; border-radius: 30px;
    background: linear-gradient(90deg, var(--symbol-mid), var(--symbol-light) 50%, var(--symbol-mid)); opacity: 0.85; }
  .symbols-after-spiritually { left: 603px; top: 388px; width: 175px; height: 50px; }
  .symbols-before-inspired { left: 319px; top: 478px; width: 178px; height: 48px; }
  .symbols-after-streetwear { left: 866px; top: 570px; width: 128px; height: 40px;
    background: linear-gradient(90deg, var(--symbol-dark), var(--symbol-light) 40%, var(--symbol-mid)); }

  .tagline { position: absolute; left: 0; top: 0; width: 1200px; height: 860px; }
  .tagline .script { font-family: 'Gochi Hand', cursive; fill: var(--ink-soft); }
  .tagline .bold { font-family: 'Fredoka', sans-serif; font-weight: 600; fill: var(--ink); }
</style>
</head>
<body>
<main class="banner">
  <div class="star-field" role="img" aria-label="Background print of scattered four-point stars and small dots in grey on black"></div>

  <header class="site-header">
    <div class="brand-name">Vorel Studios</div>
    <nav class="main-nav">
      <a class="is-current" href="#" style="left:309px">Home</a>
      <a href="#" style="left:359px">Shop</a>
      <a href="#" style="left:409px">Hoodies</a>
      <a href="#" style="left:482px">Orbit Wear</a>
      <a href="#" style="left:576px">behind the scenes</a>
      <a href="#" style="left:721px">About Us</a>
      <a href="#" style="left:801px">Contact</a>
    </nav>
    <div class="header-icons">
      <svg style="left:10px" width="20" height="20" viewBox="0 0 20 20" fill="none" stroke="#e6e6e6" stroke-width="1.5" aria-label="Search">
        <circle cx="8.5" cy="8.5" r="6.5"/><line x1="13.2" y1="13.2" x2="18.5" y2="18.5"/>
      </svg>
      <svg style="left:49px" width="20" height="20" viewBox="0 0 20 20" fill="none" stroke="#e6e6e6" stroke-width="1.5" aria-label="Cart">
        <path d="M2 5h16v11a2 2 0 0 1-2 2H4a2 2 0 0 1-2-2z"/><path d="M6.5 8V4.5a3.5 3.5 0 0 1 7 0V8"/>
      </svg>
    </div>
  </header>

  <div class="illustration planet" role="img" aria-label="Outline drawing of a ringed planet"></div>
  <div class="illustration constellation" role="img" aria-label="Constellation drawing of connected stars"></div>

  <div class="symbols symbols-after-spiritually" role="img" aria-label="Sparkle, crescent moon and hand symbols"></div>
  <div class="symbols symbols-before-inspired" role="img" aria-label="Sparkle and infinity symbols"></div>
  <div class="symbols symbols-after-streetwear" role="img" aria-label="Eye and cross symbols"></div>

  <svg class="tagline" viewBox="0 0 1200 860" aria-label="Spiritually inspired streetwear">
    <text class="script" x="209" y="434" font-size="96" textLength="378" lengthAdjust="spacingAndGlyphs">Spiritually</text>
    <text class="bold" x="512" y="533" font-size="80" textLength="357" lengthAdjust="spacingAndGlyphs">INSPIRED</text>
    <text class="script" x="416" y="610" font-size="88" textLength="440" lengthAdjust="spacingAndGlyphs">Streetwear</text>
  </svg>
</main>
</body>
</html>
```